Saffron Hearth Roti/Naan bread packaging for Australia

We would like to update and refresh the packaging design for our Saffron Hearth bread range. These breads are currently being sold in Australian supermarkets and are very popular. The proposed design should have some "continuity" with the current packaging design so that consumers can still recognise the brand/product easily on shelf. The design should suggest "fresh, tasty, healthy, authentic and Australian-made".
FYI, the products are not chilled or frozen - they sit on the regular supermarket shelves and will need to stand out. The breads will typically sit next to each other on the shelf, but usually just one facing each. I'll be uploading image files of the current packaging for your reference.
Updates

Hi all, I just uploaded the current logo for those of you who want it.  Also, there are printer details in the discussion area that you might find useful.  I am hoping to get their design template in the next day or so, but don't let that stop you from starting.  We are only looking for a design concept that we can use across the product range.  Cheers!

Hi, I've uploaded the design template/layers for those who would like this.  Cheers!

Hi everyone, thanks to those of you who have either submitted or are working on designs.  I have reviewed the available designs with the MD and will be providing individual feedback to you wherever possible.

Lastly, we'll be extending the deadline for a few more days to allow for changes and resubmissions.

Good luck everyone!

Reason: To allow for changes and resubmissions - will be providing individual feedback to all designs submitted. Cheers.

Reason: One last extension before we award the guaranteed prize.

Target Market(s)

Australian consumers who eat Indian foods and would pay a premium for a better product

Industry/Entity Type

Product

Requirements
Must have
• Transparent window to show breads
Some carryover elements from current packaging for consumer recognition
Same product info on the back (i.e. Nutritional Info panel, Heating Instructions, Barcode, Company details, Usage Suggestions)
Nice to have
• The design should suggest "fresh, tasty, healthy, authentic and Australian-made".

```html
<!DOCTYPE html>
<html lang="en">
<head>
<meta charset="utf-8">
<title>Saffron Hearth Garlic Roti – Pack Layout</title>
<link rel="stylesheet" href="https://fonts.googleapis.com/css2?family=Arimo:ital,wght@0,400;0,700;1,400;1,700&family=Tinos:ital,wght@0,400;1,400;1,700&family=PT+Sans:wght@400;700&display=swap">
<style>
:root{
  --page:#ffffff;
  --brown-deep:#3a1a0a;
  --brown-mid:#6b3518;
  --brown-warm:#8a4a22;
  --gold:#f2b01e;
  --orange:#f39a1a;
  --orange-deep:#e0711a;
  --window:#cfcfd1;
  --panel:#ffffff;
  --panel-soft:#f1eeee;
  --ink:#1b1b1b;
  --tick:#d8261c;
  --dash:#e9ddd3;
}
*{box-sizing:border-box;margin:0;padding:0}
html,body{width:1200px;height:672px;overflow:hidden;background:var(--page)}
body{font-family:"Arimo",Arial,sans-serif;color:var(--ink)}
.canvas{position:relative;width:1200px;height:672px}

.carton{position:absolute;left:32px;top:28px;width:1134px;height:608px;
  background:radial-gradient(ellipse 60% 70% at 50% 45%,var(--brown-warm) 0%,var(--brown-mid) 45%,var(--brown-deep) 100%);
  overflow:hidden}
.carton-stripes{position:absolute;inset:0;
  background:repeating-linear-gradient(90deg,rgba(0,0,0,.10) 0 18px,rgba(255,255,255,.03) 18px 40px)}
.steam{position:absolute;border-radius:50%;
  background:radial-gradient(ellipse at center,rgba(255,255,255,.22),rgba(255,255,255,0) 70%)}
.steam-left{left:250px;top:40px;width:160px;height:560px}
.steam-right{left:780px;top:20px;width:220px;height:580px}
.steam-far{left:1050px;top:20px;width:100px;height:560px}
.sunburst{position:absolute;left:340px;top:370px;width:420px;height:240px;
  background:radial-gradient(ellipse 60% 80% at 50% 100%,rgba(255,210,160,.55),rgba(180,100,50,.25) 55%,rgba(0,0,0,0) 80%)}
.guides{position:absolute;inset:0}
.glue-tab{position:absolute;bottom:0;width:40px;height:10px;background:#111}

/* left side panel */
.panel-left{position:absolute;left:127px;top:121px;width:198px;height:451px;background:var(--panel);border-radius:12px}
.versatile-title{position:absolute;left:35px;top:12px;font-family:"Tinos",serif;font-weight:400;font-size:13.5px;letter-spacing:.2px}
.versatile-list{position:absolute;left:33px;top:29px;list-style:none;font-style:italic;font-size:9.6px;line-height:12px}
.versatile-list li{display:flex;align-items:center;gap:3px}
.versatile-list svg{width:11px;height:10px;flex:none}
.nutrition{position:absolute;left:24px;top:109px;width:156px;border:1px solid #222;font-size:6.8px;line-height:8.6px}
.nutrition-head{text-align:center;border-bottom:1px solid #222;padding:2px 0;font-size:7.6px}
.nutrition-meta{padding:1px 3px;border-bottom:1px solid #222}
.nutrition table{width:100%;border-collapse:collapse;table-layout:fixed}
.nutrition th{font-weight:400;font-size:5.6px;line-height:6.6px;border-left:1px solid #222;border-bottom:1px solid #222;padding:1px 0;text-align:center}
.nutrition td{padding:0 3px;white-space:nowrap;overflow:hidden}
.nutrition td+td{text-align:center;border-left:1px solid #222;padding:0}
.ingredients{position:absolute;left:24px;top:258px;width:166px;font-size:7.9px;line-height:10.2px}
.ingredients h3{font-weight:400;font-size:10.5px;line-height:12px;margin-bottom:1px}
.best-before{position:absolute;left:24px;top:381px;width:156px;height:57px;border:1px solid #222;border-radius:6px;padding:4px;font-size:7.6px;font-weight:700}

/* front panel */
.front-frame{position:absolute;left:0;top:0}
.variant-front{position:absolute;left:371px;top:130px;color:#fff;font-size:17px;line-height:21px}
.variant-front .pieces{font-style:italic}
.variant-front .flavour{font-family:"Tinos",serif;font-style:italic;font-size:19px}
.brand-front{position:absolute;left:500px;top:138px;width:220px;text-align:center;color:var(--orange);font-weight:700;font-size:28px;line-height:32px}
.product-badge{position:absolute;left:713px;top:235px;width:99px;height:59px;border-radius:50%;
  background:#fffbe8;border:3px solid var(--gold);text-align:center;font-family:"Tinos",serif;font-style:italic;font-weight:700;color:var(--orange-deep);line-height:20px;padding-top:6px}
.product-badge .big{font-size:26px}
.product-badge .small{font-size:18px}
.cert-mark{position:absolute;left:371px;top:510px;width:47px;height:47px;border-radius:50%;background:#231208}
.net-weight{position:absolute;left:371px;top:565px;color:#fff;font-size:16.5px}
.origin-front{position:absolute;left:738px;top:571px;color:#fff;font-size:9.5px}

/* right side panel */
.brand-side{position:absolute;left:890px;top:112px;width:160px;text-align:center;color:var(--orange);font-weight:700;font-size:29px;line-height:34px}
.variant-side{position:absolute;left:890px;top:186px;width:160px;text-align:center;color:#fff;font-size:17px;line-height:22px}
.variant-side .pieces{font-style:italic}
.variant-side .flavour{font-family:"Tinos",serif;font-style:italic;font-size:19px}
.panel-right{position:absolute;left:890px;top:256px;width:159px;height:322px;background:var(--panel-soft);border-radius:10px;font-family:"PT Sans",Arial,sans-serif;font-size:10.6px;line-height:13px}
.heating{position:absolute;left:8px;top:6px;width:146px}
.heating h3{font-weight:400;font-size:10.8px;line-height:13px}
.heating p{margin-bottom:4px}
.barcode-block{position:absolute;left:10px;top:140px;width:110px;height:72px;background:#fff}
.barcode-label{position:absolute;left:6px;top:6px;width:98px;height:48px;background:#111;color:#fff;font-weight:700;font-size:13px;line-height:48px;text-align:center}
.barcode-number{position:absolute;left:0;top:55px;width:110px;text-align:center;font-size:11.5px;line-height:14px;color:#111}
.company{position:absolute;left:8px;top:222px;width:150px;font-size:10px;line-height:12px}
.company .origin{margin-bottom:5px}
</style>
</head>
<body>
<main class="canvas">
  <section class="carton">
    <div class="carton-stripes"></div>
    <div class="steam steam-left" role="img" aria-label="Soft rising steam swirls"></div>
    <div class="steam steam-right" role="img" aria-label="Soft rising steam swirls"></div>
    <div class="steam steam-far" role="img" aria-label="Soft rising steam swirls"></div>
    <div class="sunburst" role="img" aria-label="Warm sunburst rays behind the bread window"></div>
    <svg class="guides" width="1134" height="608" viewBox="0 0 1134 608">
      <g stroke="var(--dash)" stroke-width="1" stroke-dasharray="6 6" fill="none">
        <line x1="0" y1="27" x2="1134" y2="27"/>
        <line x1="0" y1="566" x2="1134" y2="566"/>
        <line x1="324" y1="0" x2="324" y2="608"/>
        <line x1="808" y1="0" x2="808" y2="608"/>
        <line x1="1072" y1="0" x2="1072" y2="608"/>
      </g>
    </svg>
    <div class="glue-tab" style="left:20px"></div>
    <div class="glue-tab" style="left:1072px"></div>
  </section>

  <aside class="panel-left">
    <h2 class="versatile-title">SO VERSATILE</h2>
    <ul class="versatile-list">
      <li><svg viewBox="0 0 11 10"><path d="M1 5 L4 9 L10 1" stroke="var(--tick)" stroke-width="2" fill="none"/></svg>Dips</li>
      <li><svg viewBox="0 0 11 10"><path d="M1 5 L4 9 L10 1" stroke="var(--tick)" stroke-width="2" fill="none"/></svg>Snacks</li>
      <li><svg viewBox="0 0 11 10"><path d="M1 5 L4 9 L10 1" stroke="var(--tick)" stroke-width="2" fill="none"/></svg>Party Needs</li>
      <li><svg viewBox="0 0 11 10"><path d="M1 5 L4 9 L10 1" stroke="var(--tick)" stroke-width="2" fill="none"/></svg>Lunch or Dinner</li>
      <li><svg viewBox="0 0 11 10"><path d="M1 5 L4 9 L10 1" stroke="var(--tick)" stroke-width="2" fill="none"/></svg>Accompaniment to Any Meal</li>
    </ul>
    <div class="nutrition">
      <div class="nutrition-head">NUTRITION INFORMATION</div>
      <div class="nutrition-meta">SERVINGS PER PACK: 6<br>SERVING SIZE: 47g</div>
      <table>
        <colgroup><col style="width:36%"><col style="width:32%"><col style="width:32%"></colgroup>
        <tr><th style="border-left:0"></th><th>Average Quantity per Serving</th><th>Average Quantity per 100g</th></tr>
        <tr><td>Energy</td><td>597KJ(143Cal)</td><td>1270KJ(303Cal)</td></tr>
        <tr><td>Protein</td><td>3.8g</td><td>8.0g</td></tr>
        <tr><td>Fat, Total</td><td>3.9g</td><td>8.3g</td></tr>
        <tr><td>&nbsp;- Saturated</td><td>1.6g</td><td>3.4g</td></tr>
        <tr><td>Carbohydrate</td><td>22.3g</td><td>47.5g</td></tr>
        <tr><td>&nbsp;- Sugar</td><td>1.7g</td><td>3.7g</td></tr>
        <tr><td>Sodium</td><td>141mg</td><td>300mg</td></tr>
      </table>
    </div>
    <div class="ingredients">
      <h3>Ingredients</h3>
      <p>Wheat Flour (Folic Acid, Thiamin), Water, Vegetable Oils (Contains Antioxidant 306 (from Soy) or 320, 319), Sugar, Garlic Powder, Gluten, Iodised Salt, Humectant (422), Mineral Salts (500, 450), Food Acid (297, 200), Cultured Dextrose, Vinegar, Yogurt Powder, Preservative (282, 202), Vegetable Gum (412), Emulsifier (481, 472e), Corn Starch.</p>
    </div>
    <div class="best-before">Best Before</div>
  </aside>

  <svg class="front-frame" width="1200" height="672" viewBox="0 0 1200 672">
    <path d="M452 136 L756 136 L756 516 L604 562 L452 516 Z" fill="none" stroke="var(--gold)" stroke-width="2.5"/>
    <rect x="445" y="132" width="42" height="34" rx="4" fill="var(--gold)" opacity=".45" role="img" aria-label="Gold filigree corner ornament"/>
    <rect x="721" y="132" width="42" height="34" rx="4" fill="var(--gold)" opacity=".45" role="img" aria-label="Gold filigree corner ornament"/>
    <rect x="556" y="544" width="96" height="24" rx="4" fill="var(--gold)" opacity=".45" role="img" aria-label="Gold filigree base ornament"/>
    <polygon points="425,254 604,212 781,254 781,456 604,502 425,456" fill="var(--window)"/>
  </svg>
  <div class="variant-front"><span class="pieces">6 Pieces</span><br><span class="flavour">Garlic</span></div>
  <div class="brand-front">Saffron<br>Hearth</div>
  <div class="product-badge"><span class="big">Roti</span><br><span class="small">Bread</span></div>
  <div class="cert-mark"></div>
  <div class="net-weight">280g NET</div>
  <div class="origin-front">MADE IN AUSTRALIA</div>

  <div class="brand-side">Saffron<br>Hearth</div>
  <div class="variant-side"><span class="pieces">6 Pieces</span><br><span class="flavour">Garlic</span></div>
  <aside class="panel-right">
    <div class="heating">
      <h3>HEATING INSTRUCTIONS<br>MICROWAVE</h3>
      <p>Lay each Roti Bread flat between paper towels and heat 10 seconds each on high.</p>
      <h3>PAN FRY</h3>
      <p>Lightly butter each side and pan fry on low heat till hot. Do not over cook to crispness.</p>
    </div>
    <div class="barcode-block">
      <div class="barcode-label">BARCODE</div>
      <div class="barcode-number">9312345 678901</div>
    </div>
    <div class="company">
      <div class="origin">MADE IN AUSTRALIA</div>
      MARLOW BAKE CO PTY LTD<br>
      14 FERRIER LANE<br>
      DANDENLEY 3172<br>
      VICTORIA.<br>
      TEL. 03 9000 1234<br>
      E-Mail: mb@marlowbake.com.au
    </div>
  </aside>
</main>
</body>
</html>
```